New locally owned rental company needs a flyer to circulate

Need flyer with logo, phone# and address. We rent cars to anyone with driver's license and proper insurance. Rates as low as $50/day. Can offer compact cars, mid-size and full size sedans. Also SUV's.

```html
<!DOCTYPE html>
<html lang="en">
<head>
<meta charset="utf-8">
<title>RoadReady Car &amp; Van Rental – Flyer</title>
<link rel="stylesheet" href="https://fonts.googleapis.com/css2?family=Montserrat:wght@400;500;600;700;800;900&display=swap">
<style>
  :root {
    --green: #2bb24c;
    --green-soft: #bfe5c6;
    --blue: #1650a8;
    --ink: #111111;
    --paper: #f2f2f0;
    --white: #ffffff;
    --car-red: #b3202c;
  }
  * { box-sizing: border-box; margin: 0; padding: 0; }
  html, body { width: 1200px; height: 768px; overflow: hidden; background: var(--paper); }
  .flyer {
    position: relative; width: 1200px; height: 768px; overflow: hidden;
    font-family: 'Montserrat', sans-serif; color: var(--ink);
    background: linear-gradient(180deg, var(--green-soft) 0%, var(--paper) 55%);
  }
  .decor { position: absolute; inset: 0; }
  .headline {
    position: absolute; left: 60px; top: 40px;
    font-weight: 900; font-size: 96px; letter-spacing: 2px; color: var(--green); line-height: 1;
  }
  .headline-rule { position: absolute; left: 60px; top: 146px; width: 560px; height: 5px; background: var(--green); }
  .fleet {
    position: absolute; left: 66px; top: 166px; width: 560px;
    font-weight: 500; font-size: 26px; line-height: 1.25;
  }
  .rate-badge { position: absolute; left: 70px; top: 245px; width: 290px; height: 290px; }
  .brand { position: absolute; left: 100px; top: 535px; }
  .brand-name { font-weight: 900; font-size: 64px; color: var(--blue); line-height: 1; letter-spacing: -1px; }
  .brand-tag { font-weight: 800; font-size: 22px; letter-spacing: 11px; margin-top: 6px; margin-left: 4px; }
  .eligibility {
    position: absolute; left: 0; top: 642px; width: 600px; height: 78px;
    background: var(--blue); color: var(--white);
    display: flex; align-items: center; justify-content: center; text-align: center;
    font-weight: 500; font-size: 22px; line-height: 1.3;
  }
  .car-photo {
    position: absolute; left: 580px; top: 170px; width: 590px; height: 250px;
    border-radius: 50% 45% 30% 30% / 60% 55% 40% 40%;
    background: radial-gradient(ellipse at 40% 55%, #d8434f 0%, var(--car-red) 45%, #5a0f16 100%);
  }
  .book-now {
    position: absolute; left: 820px; top: 440px; width: 340px; height: 62px;
    border-radius: 31px; background: var(--blue); color: var(--white);
    display: flex; align-items: center; justify-content: center;
    font-weight: 800; font-size: 34px; letter-spacing: 3px;
  }
  .contact-row { position: absolute; display: flex; align-items: center; gap: 18px; }
  .phone { left: 700px; top: 512px; height: 70px; font-weight: 700; font-size: 50px; letter-spacing: 1px; }
  .address { left: 700px; top: 600px; font-weight: 600; font-size: 26px; line-height: 1.3; }
  .address p { text-align: right; }
  .icon { width: 38px; height: 38px; flex: none; }
</style>
</head>
<body>
<main class="flyer">
  <svg class="decor" width="1200" height="768" viewBox="0 0 1200 768" aria-hidden="true">
    <polygon points="930,0 1040,0 880,260 770,260" fill="var(--green)"/>
    <polygon points="1040,0 1200,0 1200,40 1060,260 880,260" fill="var(--blue)"/>
    <polygon points="604,500 1200,500 1200,590 602,590" fill="var(--green)"/>
    <line x1="600" y1="768" x2="612" y2="420" stroke="var(--green)" stroke-width="3"/>
    <rect x="0" y="735" width="1200" height="33" fill="var(--green)"/>
  </svg>

  <h1 class="headline">RENT A CAR</h1>
  <div class="headline-rule"></div>
  <p class="fleet">We offer compact cars, mid-size, full size sedans and SUV's.</p>

  <svg class="rate-badge" viewBox="0 0 290 290" role="img" aria-label="Rates as low as $50 per day">
    <defs><path id="badge-arc" d="M45,145 A100,100 0 0 1 245,145"/></defs>
    <circle cx="145" cy="145" r="140" fill="var(--green)"/>
    <circle cx="145" cy="145" r="118" fill="none" stroke="var(--white)" stroke-width="2"/>
    <text font-family="Montserrat, sans-serif" font-size="26" font-weight="500" fill="var(--white)" letter-spacing="2">
      <textPath href="#badge-arc" startOffset="50%" text-anchor="middle">Rates as low as</textPath>
    </text>
    <polygon points="122,92 168,92 145,128" fill="var(--white)"/>
    <text x="145" y="182" text-anchor="middle" font-family="Montserrat, sans-serif" font-size="62" font-weight="800" fill="var(--ink)">$50</text>
    <text x="145" y="218" text-anchor="middle" font-family="Montserrat, sans-serif" font-size="30" font-weight="700" fill="var(--ink)">Per day</text>
  </svg>

  <div class="brand">
    <div class="brand-name">RoadReady</div>
    <div class="brand-tag">Car &amp; Van Rental</div>
  </div>

  <p class="eligibility">We rent cars to anyone with driver's<br>license and proper insurance</p>

  <div class="car-photo" role="img" aria-label="Photo of a red mid-size sedan seen from the front three-quarter view"></div>

  <div class="book-now">BOOK NOW!</div>

  <div class="contact-row phone">
    <svg class="icon" viewBox="0 0 24 24" aria-hidden="true"><path d="M6.6 10.8a15.1 15.1 0 0 0 6.6 6.6l2.2-2.2a1 1 0 0 1 1-.25 11.4 11.4 0 0 0 3.6.6 1 1 0 0 1 1 1V20a1 1 0 0 1-1 1A17 17 0 0 1 3 4a1 1 0 0 1 1-1h3.5a1 1 0 0 1 1 1c0 1.25.2 2.45.6 3.6a1 1 0 0 1-.25 1z" fill="var(--white)"/></svg>
    <span>256-555-0147</span>
  </div>

  <div class="contact-row address">
    <svg class="icon" viewBox="0 0 24 24" aria-hidden="true"><path d="M12 2a7 7 0 0 0-7 7c0 5.2 7 13 7 13s7-7.8 7-13a7 7 0 0 0-7-7zm0 9.5A2.5 2.5 0 1 1 12 6.5a2.5 2.5 0 0 1 0 5z" fill="var(--green)"/></svg>
    <p>4870B Cedar Ridge<br>Parkway Lakemont,<br>AL 36999</p>
  </div>
</main>
</body>
</html>
```